Website for Kitchen Showroom

We need a website for our Kitchen Showroom. Will be 10 pages in total. Example of a website we like can be found at http://www.brivantaform.co.uk/ with the image on the front page being a java script slideshow picking up images from a directory that I can update. Looking for simple SEO
I have the wording/ sitemap/ images all ready to go and I am looking for a quick turn around.
Thank you for your time. Tom

```html
<!DOCTYPE html>
<html lang="en">
<head>
<meta charset="utf-8">
<title>Hearthline Kitchens – Kitchen Showroom Joondalup</title>
<link rel="stylesheet" href="https://fonts.googleapis.com/css2?family=Source+Sans+3:wght@300;400;600&display=swap">
<style>
:root{
  --bg:#262626;
  --bg-light:#303030;
  --text:#d6d6d6;
  --text-dim:#9a9a9a;
  --white:#ffffff;
  --nav-top:#3a3a3a;
  --nav-bottom:#0d0d0d;
  --divider:#444;
  --link:#8fa9e0;
  --strip:#0e0e0e;
}
*{margin:0;padding:0;box-sizing:border-box}
html,body{width:1200px;height:1048px;overflow:hidden}
body{
  position:relative;
  background:radial-gradient(ellipse at 50% 40%,var(--bg-light),var(--bg) 70%);
  font-family:"Source Sans 3",sans-serif;
  color:var(--text);
}
.brand{position:absolute;left:150px;top:34px;color:var(--white);font-weight:300;line-height:1}
.brand-main{font-size:46px;letter-spacing:3px;display:block}
.brand-sub{font-size:33px;letter-spacing:5px;display:block;margin-top:6px}
.social{position:absolute;top:18px;display:flex;flex-direction:column;align-items:center;font-size:12.5px;color:var(--text)}
.social-dot{width:32px;height:32px;border-radius:50%;background:#cfcfcf;margin-bottom:4px}
.social-follow{left:936px}
.social-updates{left:1000px}
.call{position:absolute;right:158px;top:88px;font-size:27px;color:var(--white);font-weight:400}
.main-nav{
  position:absolute;left:146px;top:142px;width:906px;height:48px;
  background:linear-gradient(var(--nav-top),var(--nav-bottom) 55%);
  border-radius:4px 4px 0 0;display:flex;align-items:center;padding-left:10px;
}
.main-nav a{color:#ddd;text-decoration:none;font-size:16px;padding:0 33px;line-height:30px;border-right:1px solid #4a4a4a}
.main-nav a:last-child{border-right:none}
.main-nav a.current{font-weight:600;color:var(--white);padding-left:30px}
.slider{position:absolute;left:146px;top:209px;width:906px;height:376px;border-radius:7px;overflow:hidden;border:1px solid #bbb}
.slide-image{width:100%;height:100%;background:linear-gradient(100deg,#d9d3c7 0%,#f2efe9 30%,#c9b59a 55%,#eeece8 75%,#b7b9bb 100%)}
.slide-caption{position:absolute;left:0;top:258px;width:597px;height:83px;background:rgba(60,60,60,.78);color:var(--white);font-size:25px;line-height:27px;padding:12px 0 0 8px}
.slide-pager{position:absolute;right:0;bottom:0;display:flex}
.slide-pager span{width:34px;height:26px;background:#111;color:var(--white);font-size:12px;text-align:center;line-height:28px;border-left:1px solid #333}
.welcome{position:absolute;left:146px;top:613px;width:438px;font-size:27px;font-weight:400;color:var(--white);border-bottom:2px solid #e0e0e0;padding-bottom:2px}
.intro{position:absolute;top:657px;font-size:12.2px;line-height:16.3px;color:var(--text)}
.intro p{margin-bottom:16.3px}
.intro-left{left:146px;width:440px}
.intro-right{left:637px;width:410px}
.intro a{color:var(--link)}
.rule{position:absolute;left:146px;top:838px;width:906px;height:1px;background:var(--divider)}
.gallery-strip{position:absolute;left:146px;top:846px;width:906px;height:128px;background:linear-gradient(#1b1b1b,var(--strip));border-radius:6px}
.thumb{position:absolute;top:12px;width:155px;height:104px;border-radius:6px;border:2px solid #eee}
.thumb-sep{position:absolute;top:12px;height:104px;border-left:1px dotted #555}
.arrow{position:absolute;top:52px}
.footer{position:absolute;left:146px;top:994px;width:906px;text-align:center;font-size:10.8px;line-height:16.3px;color:var(--text-dim)}
.footer-rule{position:absolute;left:146px;top:980px;width:906px;height:1px;background:#3a3a3a}
</style>
</head>
<body>
<header>
  <div class="brand"><span class="brand-main">HEARTHLINE</span><span class="brand-sub">Kitchens</span></div>
  <div class="social social-follow"><span class="social-dot"></span>Follow</div>
  <div class="social social-updates"><span class="social-dot"></span>Updates</div>
  <div class="call">Call Today:08 6400 5127</div>
  <nav class="main-nav">
    <a class="current" href="#">Home</a><a href="#">Design</a><a href="#">Gallery</a><a href="#">Quality</a><a href="#">Contact us</a><a href="#">Links</a>
  </nav>
</header>

<section class="slider">
  <div class="slide-image" role="img" aria-label="Bright white kitchen with pendant lights, island, range and stainless steel fridge"></div>
  <div class="slide-caption">Welcome to Hearthline Kitchens. WA’s exclusive<br>kitchen manufacturer based in Joondalup Perth.</div>
  <div class="slide-pager"><span>1</span><span>2</span><span>3</span><span>4</span></div>
</section>

<h1 class="welcome">Welcome to Hearthline Kitchens</h1>
<div class="intro intro-left">
  <p>Welcome to Hearthline Kitchens. WA’s exclusive kitchen manufacturer based in Joondalup Perth. If you are seeking the highest quality kitchen, yet at a price that is a little more affordable, Hearthline Kitchens is the company you’ve been searching for.</p>
  <p>Hearthline Kitchens showroom is located less than 25 kilometers from Perth CBD, so easy to get to with easy access from the Mitchell Freeway.<br>On this site, you can view some of our designer kitchens, read testimonials from our clients or just browse through our site to find out more.</p>
</div>
<div class="intro intro-right">
  <p>We hope you will find our site inspiring and put Hearthline Kitchens at the top of your list of kitchen showrooms you simply must visit.</p>
  <p>Pop into our showroom. We can chat about your plans and ideas for your new kitchen and maybe we can give you a few ideas of our own. Or <a href="#">contact us</a> to arrange a no obligation consultation with one of our kitchen designers and if required we will bring the showroom to you.</p>
</div>

<div class="rule"></div>
<section class="gallery-strip">
  <svg class="arrow" style="left:2px" width="30" height="30" viewBox="0 0 30 30"><circle cx="15" cy="15" r="15" fill="#3a3a3a"/><path d="M17 9l-6 6 6 6" stroke="#ddd" stroke-width="3" fill="none"/></svg>
  <div class="thumb" style="left:63px;background:linear-gradient(135deg,#e8e4dc,#c82a1e 60%,#8a1a14)" role="img" aria-label="Red gloss kitchen with round table"></div>
  <div class="thumb-sep" style="left:243px"></div>
  <div class="thumb" style="left:269px;background:linear-gradient(#d8dadb,#9da4a8 70%,#3a4f8a)" role="img" aria-label="Grey kitchen with blue floor"></div>
  <div class="thumb-sep" style="left:450px"></div>
  <div class="thumb" style="left:478px;background:linear-gradient(135deg,#c3c3c3,#d35a22 50%,#8a3412)" role="img" aria-label="Orange kitchen with island"></div>
  <div class="thumb-sep" style="left:659px"></div>
  <div class="thumb" style="left:686px;background:linear-gradient(#b06a32,#e9e6e0 50%,#b7773c)" role="img" aria-label="Timber kitchen with white benchtop"></div>
  <svg class="arrow" style="left:872px" width="30" height="30" viewBox="0 0 30 30"><circle cx="15" cy="15" r="15" fill="#3a3a3a"/><path d="M13 9l6 6-6 6" stroke="#ddd" stroke-width="3" fill="none"/></svg>
</section>

<div class="footer-rule"></div>
<footer class="footer">
  © 2011 HearthlineKitchens | Unit 7/ 12 Harbour Lane Joondalup WA 6027 | TEL: 08 6400 5127 | FAX: 08 6400 5128 | EMAIL: enquiries@hearthlinekitchens.example<br>
  Hearthline Kitchens is a trading division of Westbench Holdings.
</footer>
</body>
</html>
```